Commercial Construction Interior Fitout company needs Logo and Business Cards

We need a logo and business card design. We specialise in Commercial Ceilings, Partitions, Plastering and Carpentry.

Company name: 7QX Commercial Interiors. Would like a professional looking card more than a fancy look. Gloss front preferably black pattern with Fluro Green and white text.

Will need:

Name
Position
Phone
Fax
Email
Postal Address
Web address
Updates

Thank you so much everyone for your efforts and fantastic designs..   If I didn't respond to everyone personally,  my apologises. 

Again, thanks all

R.M                               

Target Market(s)

Existing & New clients in the Construction Industry

Industry/Entity Type

Business

Requirements
Nice to have
• 7QX to be overlapped or made into some sort of Logo

```html
<!DOCTYPE html>
<html lang="en">
<head>
<meta charset="utf-8">
<title>7QX Commercial Interiors – Business Card</title>
<link href="https://fonts.googleapis.com/css2?family=Montserrat:wght@400;500;800&display=swap" rel="stylesheet">
<style>
  :root {
    --navy: #0b3f85;
    --navy-deep: #062a60;
    --navy-bright: #0d57a8;
    --paper: #ffffff;
    --paper-shade: #eef0f3;
    --stage: #e4e6ea;
    --ink: #0b3f85;
  }
  * { margin: 0; padding: 0; box-sizing: border-box; }
  html, body { width: 1200px; height: 900px; overflow: hidden; }
  body {
    background: var(--stage);
    font-family: "Montserrat", Arial, sans-serif;
    color: var(--ink);
    position: relative;
  }
  .card {
    position: absolute;
    left: 290px;
    width: 620px;
    height: 354px;
    overflow: hidden;
    box-shadow: 0 6px 18px rgba(0,0,0,0.18);
  }
  /* Back side */
  .card-back {
    top: 70px;
    background: linear-gradient(160deg, var(--navy-bright) 0%, var(--navy) 45%, var(--navy-deep) 100%);
  }
  .card-back .sheen { position: absolute; inset: 0; width: 100%; height: 100%; }
  .card-back .wordmark {
    position: absolute;
    right: 70px;
    top: 118px;
    font-weight: 800;
    font-size: 104px;
    letter-spacing: -2px;
    color: var(--paper);
    line-height: 1;
  }
  /* Front side */
  .card-front {
    top: 476px;
    background: linear-gradient(170deg, var(--paper) 0%, var(--paper-shade) 100%);
  }
  .card-front .base-band {
    position: absolute;
    left: 0; right: 0; bottom: 0;
    height: 42px;
    background: var(--navy);
  }
  .wordmark-front {
    position: absolute;
    left: 46px;
    top: 54px;
    font-weight: 800;
    font-size: 66px;
    letter-spacing: -1px;
    line-height: 1;
    color: var(--navy);
  }
  .services {
    position: absolute;
    left: 382px;
    top: 50px;
    list-style: none;
    font-size: 13.5px;
    line-height: 1.45;
  }
  .person {
    position: absolute;
    left: 46px;
    top: 170px;
  }
  .person .name { font-size: 20px; font-weight: 500; }
  .person .role { font-size: 14px; margin-top: 2px; }
  .contacts {
    position: absolute;
    left: 46px;
    top: 228px;
    list-style: none;
    font-size: 15px;
    line-height: 1.55;
  }
  .contacts li { display: flex; align-items: center; gap: 10px; }
  .contacts svg { width: 14px; height: 14px; fill: var(--navy); flex: none; }
  .address {
    position: absolute;
    left: 380px;
    top: 206px;
    padding-left: 16px;
    border-left: 1.5px solid var(--navy);
    font-size: 14.5px;
    line-height: 1.5;
    font-style: normal;
  }
</style>
</head>
<body>

  <section class="card card-back" aria-label="Card back">
    <svg class="sheen" viewBox="0 0 620 354" preserveAspectRatio="none" aria-hidden="true">
      <path d="M260 0 Q200 190 300 354 L620 354 L620 0 Z" fill="rgba(255,255,255,0.05)"/>
    </svg>
    <div class="wordmark">7QX</div>
  </section>

  <section class="card card-front" aria-label="Card front">
    <div class="wordmark-front">7QX</div>

    <ul class="services">
      <li>Commercial Ceilings</li>
      <li>Partitions</li>
      <li>Plastering and Carpentry</li>
    </ul>

    <div class="person">
      <p class="name">Daniel Marlowe</p>
      <p class="role">managing director</p>
    </div>

    <ul class="contacts">
      <li>
        <svg viewBox="0 0 14 14" aria-label="Mobile"><path d="M4 0h6a1 1 0 0 1 1 1v12a1 1 0 0 1-1 1H4a1 1 0 0 1-1-1V1a1 1 0 0 1 1-1zm0.5 1.5v9h5v-9zM7 11.5a0.8 0.8 0 1 0 0 1.6 0.8 0.8 0 0 0 0-1.6z"/></svg>
        <span>800 210 44 17</span>
      </li>
      <li>
        <svg viewBox="0 0 14 14" aria-label="Fax"><path d="M3.5 1h7v3h-7zM1 5h12a1 1 0 0 1 1 1v5h-2.5v2h-9v-2H0V6a1 1 0 0 1 1-1zm3.5 4.5v2.5h5V9.5z"/></svg>
        <span>800 210 44 18</span>
      </li>
      <li>
        <svg viewBox="0 0 14 14" aria-label="Email"><path d="M0 3h14v8H0zm1.2 1L7 8l5.8-4z"/></svg>
        <span>dmarlowe@7qx.com</span>
      </li>
    </ul>

    <address class="address">
      48 Sample Lane<br>
      Fairview, New York 10234<br>
      www.7qx.com
    </address>

    <div class="base-band"></div>
  </section>

</body>
</html>
```